Pediatric Occupational Therapy Brochure Design

This design really needs to stand out, especially with all the wordage that I have included. These brochures will be given to doctors, future clients, and caregivers. I have included the logo on by brochure, so incorporating the same or similar colors would be fantastic. A trifold brochure would probably be best to fit all the information, as this is a new business and needs to convey all the information in a way that people will read.

Target Market(s)

Doctor's offices and caregivers of children with disabilities.

Industry/Entity Type

Health Care

Font styles to use
Serif
Sans Serif

Colors
33a6d7
85acd3
ffffff
33b8a4
86cfc7

Requirements
Must have
• I would like the same colors of the logo incorporated in the brochure design.
Nice to have
• I would like to see the butterfly somehow in the background or used in the design. Also a trifold or two page design would be greatly appreciated as long as the information can fit.

```html
<!DOCTYPE html>
<html lang="en">
<head>
<meta charset="utf-8">
<title>Kinder Steps Therapy – Trifold Brochure</title>
<link rel="stylesheet" href="https://fonts.googleapis.com/css2?family=Dancing+Script:wght@700&family=Questrial&family=Open+Sans:wght@400;600;700&display=swap">
<style>
  :root{
    --teal:#7fcdd0;
    --teal-light:#b7e4e4;
    --teal-deep:#4fb6bb;
    --teal-text:#5cc3c6;
    --grey:#6d6e70;
    --grey-line:#8a8b8d;
    --ink:#1d1d1f;
    --body:#333333;
    --white:#ffffff;
    --page:#d9dadb;
    --script:'Dancing Script', cursive;
    --sans:'Questrial', sans-serif;
    --sans-bold:'Open Sans', sans-serif;
  }
  *{margin:0;padding:0;box-sizing:border-box}
  html,body{width:1200px;height:900px;overflow:hidden;background:var(--page)}
  .brochure{position:absolute;left:63px;top:65px;width:1062px;height:757px;background:var(--white);box-shadow:0 4px 14px rgba(0,0,0,.18);overflow:hidden}
  .brochure-art{position:absolute;left:0;top:0}
  .panel{position:absolute;top:0;height:757px}
  .panel--services{left:0;width:355px}
  .panel--start{left:355px;width:350px}
  .panel--cover{left:705px;width:357px}

  .services-tab{position:absolute;left:0;top:42px;width:335px;height:50px;background:var(--teal-light);border-radius:0 8px 8px 0;padding-left:28px;font:700 24px/50px var(--script);color:var(--ink);white-space:nowrap}
  .services-list{position:absolute;left:32px;top:113px;list-style:none;font:17px/20.8px var(--sans);color:var(--white);white-space:nowrap}
  .services-list li{position:relative;padding-left:16px}
  .services-list li::before{content:"";position:absolute;left:0;top:8px;width:5px;height:5px;border-radius:50%;background:var(--white)}
  .services-list .more{padding-left:10px}
  .services-list .more::before{display:none}

  .start-title{position:absolute;left:37px;top:266px;font:700 34px/1 var(--script);color:var(--ink);white-space:nowrap}
  .start-copy{position:absolute;left:37px;top:318px;width:277px;font:15.5px/19.5px var(--sans);color:var(--body);text-align:justify}
  .schedule{position:absolute;left:0;top:466px;width:350px;text-align:center;color:var(--ink)}
  .schedule-label{font:18.5px/1 var(--sans);letter-spacing:.3px}
  .schedule-call{margin-top:9px;font:700 23px/1 var(--sans-bold);display:flex;justify-content:center;align-items:center;gap:6px}
  .schedule-call svg{width:20px;height:20px}
  .hours{position:absolute;left:0;top:556px;width:350px;text-align:center;font:15px/19px var(--sans);color:var(--grey)}
  .hours-title{font:700 14.5px/19px var(--sans-bold);color:var(--ink)}
  .contact{position:absolute;left:0;top:665px;width:350px;text-align:center;color:var(--white);font:12px/16px var(--sans-bold);font-style:normal}
  .contact-name{font:600 14px/18px var(--sans-bold)}
  .contact-line{display:flex;justify-content:center;align-items:center;gap:5px}
  .contact-line svg{width:10px;height:10px}

  .brand-name{position:absolute;left:0;top:348px;width:357px;text-align:center;font:24px/1 var(--sans);color:var(--grey);padding-right:10px}
  .cover-title{position:absolute;left:0;top:526px;width:357px;text-align:center;font:700 34px/44px var(--script);color:var(--ink);white-space:nowrap}
  .cover-note{position:absolute;left:0;top:616px;width:357px;text-align:center;font:18px/1 var(--sans);color:var(--teal-text)}
  .cover-web{position:absolute;left:0;top:695px;width:357px;text-align:center;font:700 16px/1 var(--sans-bold);letter-spacing:2.2px;color:var(--ink)}
</style>
</head>
<body>
<main class="brochure">
  <svg class="brochure-art" viewBox="0 0 1062 757" width="1062" height="757">
    <defs>
      <linearGradient id="kidsTone" x1="0" y1="0" x2="1" y2="1">
        <stop offset="0" stop-color="#e9d8f0"/><stop offset=".5" stop-color="#f2c6a8"/><stop offset="1" stop-color="#9fd3e6"/>
      </linearGradient>
      <linearGradient id="girlTone" x1="0" y1="0" x2="1" y2="1">
        <stop offset="0" stop-color="#e8d6c2"/><stop offset=".6" stop-color="#c59a78"/><stop offset="1" stop-color="#f3eee8"/>
      </linearGradient>
      <linearGradient id="parkTone" x1="0" y1="0" x2="1" y2="1">
        <stop offset="0" stop-color="#dfeac9"/><stop offset=".5" stop-color="#8fbf5e"/><stop offset="1" stop-color="#e8c8b8"/>
      </linearGradient>
      <radialGradient id="lacework" cx=".5" cy=".5" r=".5">
        <stop offset=".6" stop-color="#ffffff"/><stop offset="1" stop-color="#cfd0d2"/>
      </radialGradient>
    </defs>

    <!-- services panel -->
    <rect x="0" y="0" width="355" height="757" fill="var(--teal)"/>
    <path d="M0 680 Q180 645 355 640 L355 757 L0 757 Z" fill="var(--white)"/>
    <path d="M0 680 Q180 645 355 640" fill="none" stroke="var(--grey-line)" stroke-width="3"/>
    <rect x="32" y="450" width="315" height="285" rx="10" fill="url(#kidsTone)" role="img" aria-label="Photo of a group of smiling children sitting together"/>

    <!-- header photos and swoosh -->
    <path d="M660 0 L1062 0 L1062 260 Q900 290 760 265 L680 245 Z" fill="url(#parkTone)" role="img" aria-label="Photo of a mother reading a book with two young children in a park"/>
    <path d="M355 225 Q560 170 1062 250 L1062 275 Q700 200 355 250 Z" fill="var(--teal-deep)" opacity=".9"/>
    <path d="M355 245 Q600 195 1062 272" fill="none" stroke="var(--grey-line)" stroke-width="3"/>
    <circle cx="517" cy="105" r="150" fill="var(--teal-light)"/>
    <circle cx="517" cy="105" r="139" fill="url(#girlTone)" role="img" aria-label="Photo of a cheerful girl with books at a desk"/>

    <!-- bottom bands -->
    <path d="M355 655 Q530 630 705 655 L705 757 L355 757 Z" fill="var(--teal)"/>
    <path d="M355 645 Q530 620 705 645" fill="none" stroke="var(--grey-line)" stroke-width="3"/>
    <path d="M705 670 Q880 640 1062 675 L1062 757 L705 757 Z" fill="var(--teal)"/>
    <path d="M705 660 Q880 630 1062 665" fill="none" stroke="var(--grey-line)" stroke-width="3"/>

    <!-- cover emblem -->
    <circle cx="877" cy="375" r="155" fill="url(#lacework)" role="img" aria-label="Decorative lace ornament around the emblem"/>
    <circle cx="877" cy="360" r="104" fill="var(--grey)"/>
    <circle cx="877" cy="360" r="98" fill="var(--teal-deep)"/>
    <circle cx="877" cy="360" r="88" fill="var(--white)"/>
  </svg>

  <section class="panel panel--services">
    <h2 class="services-tab">Services Offered for Your Child</h2>
    <ul class="services-list">
      <li>Social Skills</li>
      <li>Oral Motor</li>
      <li>Sensory Activities</li>
      <li>Feeding</li>
      <li>Handling Techniques</li>
      <li>Handwriting</li>
      <li>Home Exercise Program</li>
      <li>Kinesiotaping</li>
      <li>Sound-Based Listening Therapy</li>
      <li>Neuro-Developmental Treatment</li>
      <li>Patient/Parent Education</li>
      <li>Postural Reeducation</li>
      <li>Sensory Integration</li>
      <li>Therapeutic play</li>
      <li class="more">…and much more!</li>
    </ul>
  </section>

  <section class="panel panel--start">
    <h2 class="start-title">How to get started!</h2>
    <p class="start-copy">If you or someone you know has concerns about their child’s development, discuss with your doctor the concern and request a prescription for an occupational therapy evaluation.</p>
    <div class="schedule">
      <p class="schedule-label">TO SCHEDULE AN APPOINTMENT</p>
      <p class="schedule-call">CALL
        <svg viewBox="0 0 24 24"><path fill="#5cc3c6" d="M6.6 10.8a15.1 15.1 0 0 0 6.6 6.6l2.2-2.2c.3-.3.7-.4 1-.2 1.1.4 2.3.6 3.6.6.6 0 1 .4 1 1V20c0 .6-.4 1-1 1A17 17 0 0 1 3 4c0-.6.4-1 1-1h3.5c.6 0 1 .4 1 1 0 1.3.2 2.5.6 3.6.1.3 0 .7-.2 1z"/></svg>
        (555) 014-2290</p>
    </div>
    <div class="hours">
      <p class="hours-title">BUSINESS HOURS:</p>
      <p>Monday-Saturday</p>
      <p>8:00am-7:00pm</p>
    </div>
    <address class="contact">
      <p class="contact-name">Kinder Steps Therapy, LLC</p>
      <p class="contact-line"><svg viewBox="0 0 24 24"><path fill="#fff" d="M12 2a7 7 0 0 0-7 7c0 5 7 13 7 13s7-8 7-13a7 7 0 0 0-7-7zm0 9.5A2.5 2.5 0 1 1 12 6a2.5 2.5 0 0 1 0 5.5z"/></svg>48 Maple Ave, Riverton, Texas 78000</p>
      <p class="contact-line"><svg viewBox="0 0 24 24"><path fill="#fff" d="M6.6 10.8a15.1 15.1 0 0 0 6.6 6.6l2.2-2.2c.3-.3.7-.4 1-.2 1.1.4 2.3.6 3.6.6.6 0 1 .4 1 1V20c0 .6-.4 1-1 1A17 17 0 0 1 3 4c0-.6.4-1 1-1h3.5c.6 0 1 .4 1 1 0 1.3.2 2.5.6 3.6.1.3 0 .7-.2 1z"/></svg>(555) 014-2290</p>
      <p class="contact-line"><svg viewBox="0 0 24 24"><path fill="#fff" d="M2 5h20v14H2zm2 2v.5l8 5 8-5V7z"/></svg>hello@kinderstepstx.com</p>
    </address>
  </section>

  <section class="panel panel--cover">
    <p class="brand-name">Kinder Steps</p>
    <h1 class="cover-title">Pediatric Occupational<br>Therapy Services</h1>
    <p class="cover-note">(IN HOME SERVICES)</p>
    <p class="cover-web">WWW.KINDERSTEPSTX.COM</p>
  </section>
</main>
</body>
</html>
```